Animal Hospital Business Cards

Make a business card look like the attached example

*Use the same blue/black coloring
*Fenbrook Hollow Animal Hospital (instead of mobile pet rounds)
*Emergency Services (instead of tri-county care center)
*House Calls (instead of open 7 days by appointment)
*Change address to 1873 Tilden Marsh Rd Loveland, OH 45140
*Open 7 days a week (instead of emergency service)
*Add the website www.fenbrookhollowanimalhospital.example

On the back...
*instead of the text outlined in red, just white
*instead of the light blue, try your best to make it just like the blue and black on the front side of the card
*Delete "designed and printed by Blue Heron Print Co, www.blueheronprintco.example

Requirements
Must have
• look just like the attached example with requested edits/changes

```html
<!DOCTYPE html>
<html lang="en">
<head>
<meta charset="utf-8">
<title>Fenbrook Hollow Animal Hospital – Business Card</title>
<link rel="stylesheet" href="https://fonts.googleapis.com/css2?family=Red+Hat+Display:wght@500;600&display=swap">
<style>
  :root {
    --backdrop: #b1b1b1;
    --blue-deep: #0079bf;
    --blue-bright: #00bdf7;
    --square-blue: #0a86c6;
    --ink: #111111;
    --black: #000000;
    --steel: #bcbcbc;
    --white: #ffffff;
  }
  * { margin: 0; padding: 0; box-sizing: border-box; }
  html, body { width: 1200px; height: 1200px; overflow: hidden; }
  body {
    background: var(--backdrop);
    font-family: "Red Hat Display", sans-serif;
    font-weight: 500;
    color: var(--ink);
    position: relative;
  }
  .card {
    position: absolute;
    left: 208px;
    width: 784px;
    height: 480px;
    background: var(--white);
    border-radius: 34px;
    overflow: hidden;
    box-shadow: 5px 6px 6px rgba(0,0,0,0.55);
  }
  .card--front { top: 70px; }
  .card--back { top: 624px; }
  .band {
    position: absolute;
    left: 0; width: 100%;
    background: linear-gradient(90deg, var(--blue-deep) 0%, var(--blue-bright) 50%, var(--blue-deep) 100%);
    color: var(--white);
    display: flex; align-items: center; justify-content: center;
    letter-spacing: 0.5px;
  }
  .band--top { top: 0; height: 86px; font-size: 43px; }
  .band--bottom { bottom: 0; height: 87px; font-size: 45px; }
  .stripe { position: absolute; left: 0; width: 100%; height: 40px; display: block; }
  .stripe--upper { top: 86px; }
  .stripe--lower { top: 353px; }
  .line {
    position: absolute;
    left: 50%;
    transform: translate(-50%, -50%);
    white-space: nowrap;
    line-height: 1;
    text-align: center;
  }
  .doctor { font-size: 31px; }
  .species { font-size: 30px; }
  .website { font-size: 22.5px; }
  .side { position: absolute; transform: translate(-50%, -50%); text-align: center; line-height: 1.3; white-space: nowrap; }
  .side__title { font-size: 22px; line-height: 1.3; }
  .side__note { font-size: 12.5px; line-height: 1.3; margin-top: 4px; }
  .phone { font-size: 31px; }
  .row { position: absolute; white-space: nowrap; line-height: 1; transform: translateY(-50%); font-size: 30px; }
  .rule { position: absolute; height: 3px; background: var(--ink); }
  .day { position: absolute; transform: translateY(-50%); font-size: 30px; line-height: 1; display: flex; align-items: center; }
  .day::before { content: ""; width: 18px; height: 18px; background: var(--square-blue); margin-right: 4px; }
  .meridiem { position: absolute; font-size: 17px; line-height: 1; transform: translateY(-50%); }
</style>
</head>
<body>

<section class="card card--front" aria-label="Business card front">
  <div class="band band--top">Fenbrook Hollow Animal Hospital</div>
  <svg class="stripe stripe--upper" viewBox="0 0 784 40" preserveAspectRatio="none" aria-hidden="true">
    <rect width="784" height="40" fill="var(--steel)"/>
    <polygon points="0,0 784,0 0,40" fill="var(--black)"/>
  </svg>

  <p class="line doctor" style="top:160px">Marcus L. Pellington, DVM</p>

  <div class="side" style="left:85px; top:230px">
    <p class="side__title">Emergency<br>Services</p>
    <p class="side__note">1873 Tilden Marsh Rd<br>Harlow Springs, OH 45871</p>
  </div>
  <div class="side" style="left:723px; top:230px">
    <p class="side__title">House<br>Calls</p>
    <p class="side__note">30 Years<br>Of Experience</p>
  </div>

  <p class="line species" style="top:284px">Cats • Dogs • Birds • Exotics</p>
  <p class="line website" style="top:329px">www.fenbrookhollowanimalhospital.example</p>

  <svg class="stripe stripe--lower" viewBox="0 0 784 40" preserveAspectRatio="none" aria-hidden="true">
    <rect width="784" height="40" fill="var(--steel)"/>
    <polygon points="784,0 784,40 0,40" fill="var(--black)"/>
  </svg>
  <div class="band band--bottom">Open 7 days a week</div>
</section>

<section class="card card--back" aria-label="Appointment card back">
  <div class="band band--top" style="font-size:46px">Veterinary Appointment</div>

  <p class="line doctor" style="top:126px">Marcus L. Pellington, DVM</p>
  <p class="line phone" style="top:164px">513.555.0147</p>

  <p class="row" style="left:30px; top:230px">Your appointment for</p>
  <span class="rule" style="left:339px; width:343px; top:243px"></span>
  <p class="row" style="left:690px; top:230px">is on</p>

  <span class="day" style="left:28px; top:314px">Mon</span>
  <span class="day" style="left:144px; top:314px">Tues</span>
  <span class="day" style="left:265px; top:314px">Wed</span>
  <span class="day" style="left:387px; top:314px">Thur</span>
  <span class="day" style="left:505px; top:314px">Fri</span>
  <span class="day" style="left:587px; top:314px">Sat</span>
  <span class="day" style="left:683px; top:314px">Sun</span>

  <p class="row" style="left:48px; top:400px">Date</p>
  <span class="rule" style="left:122px; width:172px; top:413px"></span>
  <p class="row" style="left:406px; top:400px">Time</p>
  <span class="rule" style="left:483px; width:171px; top:413px"></span>
  <span class="meridiem" style="left:670px; top:391px">AM</span>
  <span class="meridiem" style="left:670px; top:417px">PM</span>
</section>

</body>
</html>
```